PACKAGING AND LABEL DESIGN FOR LUXURY WHISKY BRAND

We need a label and packaging design for a new luxury whisky brand based in Singapore called Morvane. We need a label design and a suggested packaging design in a box/bag or wrap form. For the bottle it is fixed, so we would like suggestions to make the bottle like a piece of art. Please refer to Harlow whisky, Kelpa Rum, PLR and Vireo coffee for the inspiration and styles we like. For the words 1746 and Oat Whisky please make original fonts or artwork. We would like it to be in Serif font but we are open to suggestions
The bottle is as attached with the following dimensions
Height :159mm
Diammeter:84mm
Outter Diameter of mouth:39mm

We develop the world's first soy wines and spirits. Our new product is a soy based whisky that pays tribute to tradition and culture in Singapore while showcasing our nation's innovative and courageous spirit, moving from a swamp to a first world nation.

Please read the brand guidelines for deeper understanding

Target Market(s)

Global travellers coming to Singapore. Adventurous, innovators and independent self made pride.

Industry/Entity Type

Alcohol beverages

Requirements
Must have
• Original label design a box/packaging design, logo of morvane, logo of 1746, fonts and art of the labels
Nice to have
• Original artwork for 1746 and Oat Whisky. Batik prints, gold, soy beans/flowers, Singapore elements.
Should not have
• No copied work.

```html
<!DOCTYPE html>
<html lang="en">
<head>
<meta charset="utf-8">
<title>Morvane 1746 Oat Whisky – Label</title>
<link rel="stylesheet" href="https://fonts.googleapis.com/css2?family=Montserrat:wght@500;600&family=Playfair+Display:ital,wght@0,700;0,900;1,700&display=swap">
<style>
  :root {
    --bg: #ffffff;
    --label-black: #111112;
    --pattern-grey: #1e1e20;
    --gold-light: #f7df86;
    --gold-mid: #d9aa3c;
    --gold-deep: #9a6b14;
    --gold-text: #d2a84a;
    --ivory: #f6f3ec;
  }
  html, body {
    margin: 0;
    width: 1200px;
    height: 1200px;
    overflow: hidden;
    background: var(--bg);
  }
  .label {
    display: block;
    width: 1200px;
    height: 1200px;
  }
  .brand-mark {
    font-family: "Montserrat", sans-serif;
    font-weight: 600;
    font-size: 24px;
    letter-spacing: 4px;
    fill: var(--gold-text);
  }
  .brand-name {
    font-family: "Montserrat", sans-serif;
    font-weight: 500;
    font-size: 60px;
    letter-spacing: 18px;
    fill: var(--gold-text);
  }
  .possessive {
    font-family: "Montserrat", sans-serif;
    font-weight: 500;
    font-size: 32px;
    letter-spacing: 8px;
    fill: var(--ivory);
  }
  .year {
    font-family: "Playfair Display", serif;
    font-weight: 900;
    font-size: 160px;
    letter-spacing: 4px;
  }
  .product-name {
    font-family: "Playfair Display", serif;
    font-weight: 900;
    font-size: 60px;
    letter-spacing: 1px;
    word-spacing: 14px;
    fill: var(--ivory);
  }
  .quality-script {
    font-family: "Playfair Display", serif;
    font-style: italic;
    font-weight: 700;
    font-size: 20px;
    fill: var(--gold-text);
  }
  .quality-caps {
    font-family: "Montserrat", sans-serif;
    font-weight: 500;
    font-size: 15px;
    letter-spacing: 4px;
    fill: var(--ivory);
  }
  .origin {
    font-family: "Montserrat", sans-serif;
    font-weight: 600;
    font-size: 27px;
    letter-spacing: 3px;
    fill: var(--gold-text);
  }
</style>
</head>
<body>
<svg class="label" viewBox="0 0 1200 1200" xmlns="http://www.w3.org/2000/svg">
  <defs>
    <linearGradient id="goldFoil" x1="0" y1="0" x2="1" y2="1">
      <stop offset="0" stop-color="var(--gold-deep)"/>
      <stop offset="0.3" stop-color="var(--gold-light)"/>
      <stop offset="0.55" stop-color="var(--gold-mid)"/>
      <stop offset="0.8" stop-color="var(--gold-light)"/>
      <stop offset="1" stop-color="var(--gold-deep)"/>
    </linearGradient>
    <linearGradient id="yearFoil" x1="0" y1="0" x2="0" y2="1">
      <stop offset="0" stop-color="var(--gold-light)"/>
      <stop offset="0.5" stop-color="var(--gold-mid)"/>
      <stop offset="1" stop-color="var(--gold-deep)"/>
    </linearGradient>
    <radialGradient id="patternGlow" cx="0.5" cy="0.5" r="0.7">
      <stop offset="0" stop-color="var(--label-black)"/>
      <stop offset="1" stop-color="var(--pattern-grey)"/>
    </radialGradient>
    <clipPath id="labelInner">
      <path d="M250 212 Q250 192 270 192 L486 192 A115 115 0 0 1 714 192 L930 192 Q950 192 950 212 L950 1033 L638 1110 L562 1110 L250 1033 Z"/>
    </clipPath>
  </defs>

  <!-- gold frame -->
  <path class="label-frame" fill="url(#goldFoil)"
        d="M240 202 Q240 182 260 182 L477 182 A125 125 0 0 1 723 182 L940 182 Q960 182 960 202 L960 1040 L640 1120 L560 1120 L240 1040 Z"/>

  <!-- black field -->
  <path class="label-field" fill="var(--label-black)"
        d="M250 212 Q250 192 270 192 L486 192 A115 115 0 0 1 714 192 L930 192 Q950 192 950 212 L950 1033 L638 1110 L562 1110 L250 1033 Z"/>

  <!-- deco pattern area -->
  <g clip-path="url(#labelInner)">
    <rect class="deco-pattern" x="250" y="70" width="700" height="1050" fill="url(#patternGlow)"
          role="img" aria-label="Faint grey art deco geometric line pattern across the label field"/>
  </g>

  <!-- brand name in place of the mark -->
  <text class="brand-mark" x="602" y="150" text-anchor="middle">MORVANE</text>

  <text class="brand-name" x="609" y="388" text-anchor="middle">MORVANE</text>

  <text class="possessive" x="604" y="532" text-anchor="middle">MORVANE'S</text>
  <text class="year" x="602" y="668" text-anchor="middle" fill="url(#yearFoil)">1746</text>
  <text class="product-name" x="600" y="744" text-anchor="middle">OAT WHISKY</text>

  <text class="quality-script" x="600" y="912" text-anchor="middle">Premium</text>
  <text class="quality-caps" x="602" y="932" text-anchor="middle">QUALITY</text>

  <!-- origin bracket -->
  <path class="origin-frame" fill="none" stroke="url(#goldFoil)" stroke-width="2"
        d="M385 968 L815 968 L830 990 L815 1012 L385 1012 L370 990 Z"/>
  <text class="origin" x="600" y="1000" text-anchor="middle">MADE IN SINGAPORE</text>
</svg>
</body>
</html>
```